依頼詳細
縦レイアウトを希望します。(文字は横)
コンサルタントとしてみていただけるような迫力のある名刺を作りたいです。
記載項目
青葉総合管理株式会社
代表取締役 村田 浩二
東京都中央区湊3丁目7番2号第1柏木ビル4F
TEL03-5244-9860 FAX03-5244-9860
murata@aobakanri-demo.jp
東京都知事(3)第71268号
希望イメージ
• +5 0 +5
• シンプル
複雑
• 単色
カラフル
• 暗い
明るい
• 日常
高級
• 遊び心
厳粛
• 未来的
伝統的
• 女性的
男性的
希望する色
シルバー
納品ファイル
• イラストレーター形式 (.ai)
補足説明
会社ロゴを銀色にしたいです。

シンプルで、伝えたいことを伝えやすい
もらった人がありがたく感じる名刺になると感じました。
自分自身もありがたいと思っていただける人間になります。

皆様、お忙しい中、ありがとうございました。
いろいろなご提案をいただき、選択の幅を広く持つことができました。
次回またよろしくお願いいたします。

```html
<!DOCTYPE html>
<html lang="ja">
<head>
<meta charset="utf-8">
<title>青葉総合管理株式会社 名刺</title>
<link rel="stylesheet" href="https://fonts.googleapis.com/css2?family=Noto+Sans+JP:wght@400;500&display=swap">
<style>
  :root {
    --backdrop: #e4e4e4;
    --card: #ffffff;
    --ink: #666666;
    --ink-soft: #7a7a7a;
    --silver: #a3a3a3;
  }
  * { margin: 0; padding: 0; box-sizing: border-box; }
  html, body { width: 1148px; height: 1200px; overflow: hidden; }
  body {
    background: var(--backdrop);
    font-family: "Noto Sans JP", sans-serif;
    color: var(--ink);
    position: relative;
  }
  .card {
    position: absolute;
    left: 284px; top: 120px;
    width: 580px; height: 960px;
    background: var(--card);
  }
  .card > * { position: absolute; left: 52px; white-space: nowrap; }
  .brand-mark {
    left: 55px; top: 54px;
    width: 144px; height: 144px;
    border-radius: 50%;
    background: var(--silver);
  }
  .brand-name {
    left: 55px; top: 198px; width: 144px;
    text-align: center;
    font-size: 42px; font-weight: 400;
    letter-spacing: 0.04em;
    color: var(--silver);
  }
  .role { top: 318px; font-size: 19px; font-weight: 500; }
  .person-name { top: 362px; font-size: 36px; font-weight: 500; letter-spacing: 0.25em; }
  .person-roman { top: 435px; font-size: 18px; letter-spacing: 0.08em; color: var(--ink-soft); }
  .company { top: 542px; font-size: 23px; font-weight: 500; letter-spacing: 0.15em; }
  .postal { top: 580px; font-size: 15px; color: var(--ink-soft); }
  .address { top: 606px; font-size: 18px; line-height: 34px; }
  .contact { top: 688px; list-style: none; }
  .contact li { display: flex; align-items: baseline; height: 34px; }
  .contact .label { width: 54px; font-size: 14px; letter-spacing: 0.3em; color: var(--ink-soft); }
  .contact .value { font-size: 25px; letter-spacing: 0.04em; }
  .license { top: 884px; font-size: 16px; font-weight: 500; }
</style>
</head>
<body>
  <section class="card" aria-label="青葉総合管理株式会社 名刺 表面">
    <div class="brand-mark" aria-hidden="true"></div>
    <div class="brand-name">AOBA</div>

    <p class="role">代表取締役</p>
    <h1 class="person-name">村田 浩二</h1>
    <p class="person-roman">KOJI MURATA</p>

    <p class="company">青葉総合管理株式会社</p>
    <p class="postal">104-0043</p>
    <p class="address">東京都中央区湊3丁目7番2号<br>第1柏木ビル4F</p>

    <ul class="contact">
      <li><span class="label">TEL</span><span class="value">03 6187 2405</span></li>
      <li><span class="label">FAX</span><span class="value">03 6187 2406</span></li>
      <li><span class="label" style="letter-spacing:0.05em">CELL</span><span class="value">090 4821 3375</span></li>
      <li><span class="label" style="letter-spacing:0.05em">MAIL</span><span class="value">murata@aobakanri-demo.jp</span></li>
      <li><span class="label">URL</span><span class="value">aobakanri-demo.jp</span></li>
    </ul>

    <p class="license">免許番号：東京都知事(3)第71268号</p>
  </section>
</body>
</html>
```